K.T.L Electrical Services Pty Ltd

Electrical contracting business. I have a base for the design which i like. The contact number needs to be changed to 0491736250 and the O made more solid and level with the rest of the letters. If you have any other ideas of what would make it better I'm happy to see them.

The back side to be written as dot points with the following:
- Residential & Commercial
- Maintenance
- PV & Battery servicing
- EV Chargers

```html
<!DOCTYPE html>
<html lang="en">
<head>
<meta charset="utf-8">
<title>K.T.L Electrical Services – Business Card</title>
<link rel="stylesheet" href="https://fonts.googleapis.com/css2?family=Montserrat:wght@400;500;700&display=swap">
<style>
  :root {
    --backdrop: #1f2a2f;
    --card-white: #ffffff;
    --ink-dark: #1f2b30;
    --sage: #8fa9a9;
    --back-deep: #101b21;
    --back-mid: #1e2c33;
  }
  * { margin: 0; padding: 0; box-sizing: border-box; }
  html, body {
    width: 1200px; height: 1200px; overflow: hidden;
    background: var(--backdrop);
    font-family: "Montserrat", sans-serif;
  }
  .canvas { position: relative; width: 1200px; height: 1200px; }

  .card {
    position: absolute; left: 165px; width: 908px; height: 518px;
    border-radius: 62px; overflow: hidden;
    box-shadow: 0 6px 24px rgba(0, 0, 0, 0.35);
  }
  .card--front { top: 52px; background: var(--card-white); }
  .card--back { top: 607px; }

  .company-name {
    position: absolute; left: 81px; top: 86px;
    font-size: 40px; font-weight: 700; color: var(--ink-dark);
    letter-spacing: 0.2px; white-space: nowrap;
  }
  .contact-line {
    position: absolute; left: 83px; top: 152px;
    display: flex; align-items: center; gap: 20px;
    color: var(--sage); font-size: 36px; font-weight: 400;
  }
  .contact-line svg { width: 30px; height: 30px; fill: var(--sage); }

  .brand-name {
    position: absolute; right: 48px;
    color: var(--sage); font-size: 24px; font-weight: 700;
    white-space: nowrap; line-height: 1;
  }
  .card--front .brand-name { top: 392px; }
  .card--back .brand-name { top: 401px; }

  .back-texture {
    position: absolute; inset: 0;
    background:
      radial-gradient(ellipse at 55% 60%, rgba(40, 58, 64, 0.55) 0%, rgba(40, 58, 64, 0) 65%),
      linear-gradient(135deg, var(--back-deep) 0%, var(--back-mid) 55%, var(--back-deep) 100%);
  }
  .service-list {
    position: absolute; left: 56px; top: 96px; list-style: none;
    color: var(--sage); font-size: 29px; font-weight: 500;
  }
  .service-list li {
    position: relative; padding-left: 31px; height: 46px; line-height: 46px;
  }
  .service-list li::before {
    content: ""; position: absolute; left: 0; top: 16px;
    width: 14px; height: 14px; border-radius: 50%; background: var(--sage);
  }
</style>
</head>
<body>
<main class="canvas">
  <section class="card card--front">
    <h1 class="company-name">K.T.L Electrical Services</h1>
    <p class="contact-line">
      <svg viewBox="0 0 24 24" aria-hidden="true"><path d="M6.6 10.8a15.1 15.1 0 0 0 6.6 6.6l2.2-2.2a1 1 0 0 1 1-.25 11.4 11.4 0 0 0 3.6.57 1 1 0 0 1 1 1V20a1 1 0 0 1-1 1A17 17 0 0 1 3 4a1 1 0 0 1 1-1h3.5a1 1 0 0 1 1 1c0 1.25.2 2.45.57 3.6a1 1 0 0 1-.25 1z"/></svg>
      <span>0491736250</span>
    </p>
    <p class="brand-name">K.T.L Electrical Services P/L</p>
  </section>

  <section class="card card--back">
    <div class="back-texture" role="img" aria-label="Faint repeating brand pattern across a dark slate background"></div>
    <ul class="service-list">
      <li>Residential &amp; Commercial</li>
      <li>Maintenance</li>
      <li>PV &amp; Battery servicing</li>
      <li>EV Chargers</li>
    </ul>
    <p class="brand-name">K.T.L Electrical Services P/L</p>
  </section>
</main>
</body>
</html>
```